vireo nuts company small package

we are looking to design a package for our nuts 10cm by 13 cm and also 3.25 inch by 4.5 inches. our nuts are:
Salted peanuts
honey roasted peanuts
salted cashews
honey roasted cashews
pistachios
sunflower seeds

have a floral design simple yet elegant not too crowded
our product is non GMO

some of our competitors:
http://kestrabite.example/
http://www.dovuhusk.example/sg/
http://tirotiro.example/en/content/view/5/17/

Target Market(s)

european market, Middle eastern market

Industry/Entity Type

It Company

Font styles to use
Decorative
Script

Requirements
Must have
• floral design not crowded yet elegant
• high resolution pictures of the nuts
Nice to have
Should not have
• cartoon characters

```html
<!DOCTYPE html>
<html lang="en">
<head>
<meta charset="utf-8">
<title>Vireo Salted Peanuts – Package Front</title>
<link rel="stylesheet" href="https://fonts.googleapis.com/css2?family=Days+One&family=Parisienne&display=swap">
<style>
  :root {
    --teal-deep: #0a3a52;
    --teal-mid: #0f5a78;
    --teal-light: #1a6f8f;
    --gold: #d9c07e;
    --gold-dark: #a88a44;
    --gold-light: #f1e3b4;
    --silver: #e8ecee;
    --plaque-white: #ffffff;
    --plaque-shade: #d9dde0;
    --brand-blue: #1478a8;
    --peanut-light: #e9cfa3;
    --peanut-mid: #c99a5e;
    --peanut-dark: #8c6236;
    --script-white: #ffffff;
  }
  html, body {
    margin: 0;
    padding: 0;
    width: 867px;
    height: 1200px;
    overflow: hidden;
    background: var(--teal-deep);
  }
  .package-front {
    position: relative;
    width: 867px;
    height: 1200px;
    overflow: hidden;
  }
  .package-art {
    position: absolute;
    inset: 0;
    display: block;
  }
  .brand-name {
    font-family: "Days One", "Arial Black", sans-serif;
    font-size: 112px;
    fill: var(--brand-blue);
    letter-spacing: 2px;
  }
  .variety-line {
    font-family: "Parisienne", cursive;
    fill: var(--script-white);
    filter: drop-shadow(2px 3px 2px rgba(0,0,0,0.45));
  }
  .variety-salted { font-size: 86px; }
  .variety-peanuts { font-size: 170px; }
</style>
</head>
<body>
<main class="package-front">
  <svg class="package-art" width="867" height="1200" viewBox="0 0 867 1200" xmlns="http://www.w3.org/2000/svg">
    <defs>
      <linearGradient id="bgTeal" x1="0" y1="0" x2="0" y2="1">
        <stop offset="0" stop-color="var(--teal-deep)"/>
        <stop offset="0.45" stop-color="var(--teal-mid)"/>
        <stop offset="0.75" stop-color="var(--teal-light)"/>
        <stop offset="1" stop-color="var(--teal-deep)"/>
      </linearGradient>
      <linearGradient id="goldBand" x1="0" y1="0" x2="0" y2="1">
        <stop offset="0" stop-color="var(--gold-light)"/>
        <stop offset="0.5" stop-color="var(--gold)"/>
        <stop offset="1" stop-color="var(--gold-dark)"/>
      </linearGradient>
      <linearGradient id="goldStroke" x1="0" y1="0" x2="1" y2="1">
        <stop offset="0" stop-color="var(--gold-dark)"/>
        <stop offset="0.5" stop-color="var(--gold-light)"/>
        <stop offset="1" stop-color="var(--gold-dark)"/>
      </linearGradient>
      <radialGradient id="plaqueFill" cx="0.5" cy="0.4" r="0.7">
        <stop offset="0" stop-color="var(--plaque-white)"/>
        <stop offset="0.7" stop-color="#f1f3f4"/>
        <stop offset="1" stop-color="var(--plaque-shade)"/>
      </radialGradient>
      <radialGradient id="filigreeGlow" cx="0.5" cy="0.5" r="0.5">
        <stop offset="0.55" stop-color="var(--gold)" stop-opacity="0.55"/>
        <stop offset="1" stop-color="var(--gold)" stop-opacity="0"/>
      </radialGradient>
      <radialGradient id="peanutPhoto" cx="0.5" cy="0.55" r="0.65">
        <stop offset="0" stop-color="var(--peanut-light)"/>
        <stop offset="0.6" stop-color="var(--peanut-mid)"/>
        <stop offset="1" stop-color="var(--peanut-dark)"/>
      </radialGradient>
      <linearGradient id="bottomPanel" x1="0" y1="0" x2="0" y2="1">
        <stop offset="0" stop-color="var(--teal-light)"/>
        <stop offset="1" stop-color="var(--teal-deep)"/>
      </linearGradient>
    </defs>

    <!-- background -->
    <rect class="background" width="867" height="1200" fill="url(#bgTeal)"/>

    <!-- horizontal gold band with silver edges -->
    <g class="header-band">
      <rect x="0" y="196" width="867" height="96" fill="var(--silver)"/>
      <rect x="0" y="203" width="867" height="82" fill="url(#goldBand)"/>
    </g>

    <!-- filigree ornament area around the plaque -->
    <ellipse class="filigree-ornament" role="img" aria-label="Gold floral filigree ornament framing the brand plaque"
             cx="433" cy="245" rx="245" ry="185" fill="url(#filigreeGlow)"/>

    <!-- brand plaque -->
    <g class="brand-plaque">
      <path d="M433,108 C520,108 600,120 640,140 C660,170 668,210 668,245 C668,280 660,320 640,350 C600,370 520,382 433,382 C346,382 266,370 226,350 C206,320 198,280 198,245 C198,210 206,170 226,140 C266,120 346,108 433,108 Z"
            fill="url(#goldStroke)"/>
      <path d="M433,122 C516,122 590,133 628,151 C646,178 652,214 652,245 C652,276 646,312 628,339 C590,357 516,368 433,368 C350,368 276,357 238,339 C220,312 214,276 214,245 C214,214 220,178 238,151 C276,133 350,122 433,122 Z"
            fill="url(#plaqueFill)"/>
      <text class="brand-name" x="433" y="286" text-anchor="middle">VIREO</text>
    </g>

    <!-- arched product window -->
    <g class="product-window">
      <path d="M104,1000 V760 C104,560 258,470 441,470 C624,470 778,560 778,760 V1000 Z"
            fill="url(#goldStroke)"/>
      <path class="product-photo" role="img" aria-label="Close-up photograph of salted roasted peanuts"
            d="M118,1000 V760 C118,572 266,484 441,484 C616,484 764,572 764,760 V1000 Z"
            fill="url(#peanutPhoto)"/>
    </g>

    <!-- lower wave panel -->
    <path class="bottom-panel" d="M-10,1012 C180,905 320,858 441,858 C570,858 720,915 877,1000 V1210 H-10 Z"
          fill="url(#bottomPanel)" stroke="url(#goldStroke)" stroke-width="9"/>

    <!-- variety name -->
    <g class="variety-name">
      <text class="variety-line variety-salted" x="398" y="958" text-anchor="middle" transform="rotate(-12 398 958)">Salted</text>
      <text class="variety-line variety-peanuts" x="425" y="1092" text-anchor="middle" transform="rotate(-8 425 1092)">Peanuts</text>
    </g>
  </svg>
</main>
</body>
</html>
```